Letterhead Design for Law Firm

**Edit: I have added the photo of a bottom that I like.

------
We are looking for a re-design of our new letterhead. The letterhead is for a law firm and will be used for digital and traditionally printed correspondence.

Here are some suggestions:

- Please use colours are #8ec900 and simple black.
- Please do not use any type of "waves" at the bottom of the page. This is not in style at all.
- Please stay modern yet conservative.
- Please use font Segoe UI Light or similar if you can
- Avoid clipart or illustrations.
- Utilize ample white space in the layout so the design looks clean and information is easy to read at a glance. Don't overcrowd the letterhead.
- Make sure the letterhead design is consistent with our brand identity (see brambleford.ca)
-Please, no black headers or footers.

I am attaching my current letterhead and signature for your convenience.

Remember, the letterhead is an extension of our professional identity. We are a successful firm and trial lawyers who correspond with insurers, judges, lawyers, courts, clients, etc. Make it new, modern, attractive, yet powerful and conservative.

It needs to be easily printable. I would like the bleed removed in print so the black bar the bottom crosses the page (but the text is not near the edges)

Target Market(s)

Clients, Government Offices, Judiciary, Lawyers, Insurance Companies, Colleagues.

Industry/Entity Type

Law

Font styles to use
Other font styles liked:
• Segoe UI LIght, Calibri Light,

Colors
00AB8E
00BBA5
67D7C9
C6EFE9
E9F9F6

Requirements
Must have
• Everything that is on the letterhead now.
Nice to have
• Cutting Edge design, yet conservative.
Should not have
• law firm cliche design, images,

```html
<!DOCTYPE html>
<html lang="en">
<head>
<meta charset="utf-8">
<title>Ferrand Letterhead</title>
<link rel="stylesheet" href="https://fonts.googleapis.com/css2?family=Arimo:wght@400;700&family=Mulish:wght@600;700&display=swap">
<style>
  :root {
    --brand-green: #8ec900;
    --ink: #111111;
    --text-grey: #555555;
    --heading-grey: #4a4a4a;
    --rule-grey: #bdbdbd;
    --paper: #ffffff;
  }
  * { box-sizing: border-box; margin: 0; padding: 0; }
  html, body { width: 1189px; height: 1200px; overflow: hidden; background: var(--paper); }
  .letterhead {
    position: relative;
    width: 1189px;
    height: 1200px;
    background: var(--paper);
    font-family: "Arimo", Arial, sans-serif;
    color: var(--text-grey);
  }
  .masthead { position: absolute; top: 0; left: 0; width: 100%; height: 160px; }
  .firm-name {
    position: absolute; left: 106px; top: 74px;
    display: flex; align-items: center; gap: 12px;
    font-family: "Arimo", Arial, sans-serif;
    font-weight: 700; font-size: 34px; line-height: 40px;
    color: var(--ink);
  }
  .firm-name .marker { width: 18px; height: 18px; background: var(--brand-green); flex: none; }
  .green-band { position: absolute; left: 0; right: 0; top: 140px; height: 11px; background: var(--brand-green); }
  .black-rule { position: absolute; left: 0; right: 0; top: 155px; height: 2px; background: var(--ink); }
  .divider { position: absolute; top: 56px; width: 1px; height: 72px; background: var(--rule-grey); }
  .divider.first { left: 491px; }
  .divider.second { left: 764px; }
  .contact-list { position: absolute; left: 553px; top: 58px; list-style: none; font-size: 17px; line-height: 23px; color: var(--text-grey); }
  .contact-list li { display: flex; align-items: center; gap: 6px; }
  .contact-list svg { width: 14px; height: 14px; flex: none; }
  .address { position: absolute; left: 817px; top: 58px; font-style: normal; font-size: 17px; line-height: 23px; }
  .letter-body { position: absolute; left: 106px; top: 320px; width: 1000px; }
  .salutation { font-family: "Mulish", sans-serif; font-weight: 700; font-size: 25px; color: var(--heading-grey); margin-bottom: 36px; }
  .letter-body p.paragraph { font-size: 18.5px; line-height: 24.5px; margin-bottom: 22px; white-space: nowrap; }
  .closing { font-family: "Mulish", sans-serif; font-weight: 700; font-size: 15px; color: var(--heading-grey); margin-top: 34px; }
  .signature-block { position: absolute; left: 705px; top: 960px; }
  .signature-mark { width: 355px; height: 70px; background: linear-gradient(90deg, #f4f4f4, #e6e6e6); border-bottom: 1.5px solid var(--ink); }
  .signer-name { margin-top: 22px; font-weight: 700; font-size: 18px; color: var(--brand-green); }
  .signer-firm { font-size: 18px; line-height: 24px; color: var(--text-grey); }
</style>
</head>
<body>
<main class="letterhead">
  <header class="masthead">
    <div class="firm-name"><span class="marker"></span>Ferrand</div>
    <div class="green-band"></div>
    <div class="black-rule"></div>
    <span class="divider first"></span>
    <ul class="contact-list">
      <li><svg viewBox="0 0 14 14"><path fill="#8ec900" d="M3 1.5l2 .3 1 3-1.4 1.1a7 7 0 0 0 3.5 3.5L9.2 8l3 1 .3 2-1.6 1.6C6.5 12.4 1.6 7.5 1.4 3.1z"/></svg>905-555-0142</li>
      <li><svg viewBox="0 0 14 14"><rect x="1" y="3" width="12" height="8" fill="#8ec900"/><path d="M1.5 3.5 7 8l5.5-4.5" stroke="#fff" stroke-width="1.2" fill="none"/></svg>info@brambleford.ca</li>
      <li><svg viewBox="0 0 14 14"><circle cx="7" cy="7" r="6" fill="#8ec900"/><path d="M1 7h12M7 1c-2.5 3-2.5 9 0 12M7 1c2.5 3 2.5 9 0 12" stroke="#fff" stroke-width="1" fill="none"/></svg>www.brambleford.ca</li>
    </ul>
    <span class="divider second"></span>
    <address class="address">48 Wexley Street West<br>Suite 1210<br>Hamilton, ON L8P 2C7, Canada</address>
  </header>

  <section class="letter-body">
    <h1 class="salutation">Dear Mr. Smith,</h1>
    <p class="paragraph">Lorem ipsum dolor sit amet, consectetuer adipiscing elit, sed diam nonmmy nibh euismod tincidunt ut laor<br>eet dolore magna aliquam erat volutpat. Ut wisi enim ad minim veniam, quis nostrud exerci tationmcorper<br>suscipit lobortis nisl ut aliquip ex ea commodo consequat. Duis autem vel eum iriure dolor in hendrerit in<br>vulputate velit esse molestie consequat, vel illum dolore eu feugiat</p>
    <p class="paragraph">Rorem ipsum dolor sit amet, consectetuer adipiscing elit, sed diam nonmmy nibh euismod tincidunt ut laor<br>eet dolore magna aliquam erat volutpat. Ut wisi enim ad minim veniam, quis nostrud exerci tationmcorper<br>suscipit lobortis nisl ut aliquip ex ea commodo consequat. Duis autem vel eum iriure dolor in hendrerit in<br>vulputate velit esse molest</p>
    <p class="paragraph">Dorem ipsum dolor sit amet, consectetuer adipiscing elit, sed diam nonmmy nibh euismod tincidunt ut laor<br>eet dolore magna aliquam erat volutpat. Ut wisi enim ad minim veniam, quis nostrud exerci tationmcorper<br>suscipit lobortis nisl ut aliquip ex ea commodo consequat. Duis autem vel eum iriure dolor in hendrerit in<br>suscipit lobortis nisl ut aliquip ex ea commodo consequat. Duis autem vel eum iriure dolor in hendrerit in<br>vulputate velit esse molestie consequat, vel illum</p>
    <p class="paragraph">Sorem ipsum dolor sit amet, consectetuer adipiscing elit, sed diam nonmmy nibh euismod tincidunt ut laor<br>eet dolore magna aliquam erat volutpat. Ut wisi enim ad minim veniam, quis nostrud exerci tationmcorper<br>suscipit lobortis nisl ut aliquip ex ea commodo consequat. Duis autem vel eum iriure dolor in</p>
    <p class="closing">Sincerely,</p>
  </section>

  <section class="signature-block">
    <div class="signature-mark" role="img" aria-label="Handwritten signature of Paul D. Ferrand"></div>
    <p class="signer-name">Paul D. Ferrand</p>
    <p class="signer-firm">Ferrand Law Professional Corporation</p>
  </section>
</main>
</body>
</html>
```